Verdant Loop Advisors, LLC

I am looking for a simple, clear layout with my logo prominent and embossed, on the best quality card stock available. I would like the business name and phone number included on the card as well......I dont want my name anywhere on the card and I would like my logo embossed on the card......something simple with a white back......open to designs as long as they go along with recycling symbols and green type stuff.....The address, website, cell number, fax number, and email are listed below

5374 Tillbury Fenwood Road
Ashcombe Vale, QX 10101

c. 555.555.0143 f. 555.555.0187
e. sales@verdantloopadvisors.example
w. www.verdantloopadvisors.example

Industry/Entity Type

Recycling

```html
<!DOCTYPE html>
<html lang="en">
<head>
<meta charset="utf-8">
<title>Verdant Loop Advisors, LLC – Business Card</title>
<link rel="stylesheet" href="https://fonts.googleapis.com/css2?family=Michroma&family=Mulish:wght@400&display=swap">
<style>
  :root {
    --backdrop: #625d5d;
    --card: #ffffff;
    --card-edge: #3b3838;
    --brand-green: #1f7a35;
    --label-green: #2a7a3c;
    --ink: #1d1d1d;
    --band-start: #edf3ee;
    --band-end: #f7f9f7;
    --band-line: #ffffff;
    --band-shadow: #e6ede7;
    --pin-red: #e2232a;
    --watermark: #e8f0e9;
  }
  * { box-sizing: border-box; margin: 0; padding: 0; }
  html, body {
    width: 1200px; height: 1000px; overflow: hidden;
    background: var(--backdrop);
  }
  .business-card {
    position: absolute;
    left: 213px; top: 266px;
    width: 782px; height: 448px;
    background: linear-gradient(160deg, #f3f7f4 0%, var(--card) 45%, #f6f9f6 100%);
    border: 1px solid var(--card-edge);
    overflow: hidden;
  }
  .watermark-disc {
    position: absolute;
    left: 508px; top: 120px;
    width: 270px; height: 270px;
    border-radius: 50%;
    background: var(--watermark);
    opacity: .75;
  }
  .brand {
    position: absolute;
    left: 0; right: 0; top: 24px;
    display: flex; align-items: center; justify-content: center; gap: 14px;
  }
  .brand-dot {
    width: 54px; height: 54px; border-radius: 50%;
    background: var(--brand-green);
    flex: none;
  }
  .brand-name {
    font-family: "Michroma", sans-serif;
    font-weight: 400;
    font-size: 22px;
    letter-spacing: 1px;
    color: var(--ink);
    white-space: nowrap;
  }
  .contact-list { list-style: none; }
  .contact-row {
    position: absolute;
    left: 8px; height: 54px;
    display: flex; align-items: center;
    padding-left: 12px;
    font-family: "Mulish", sans-serif;
    font-size: 17px;
    white-space: nowrap;
  }
  .contact-row::before {
    content: "";
    position: absolute;
    left: 0; top: 0; bottom: 0;
    width: var(--band-width);
    background: linear-gradient(90deg, var(--band-start), var(--band-end));
    border-top: 2px solid var(--band-line);
    border-bottom: 2px solid var(--band-shadow);
    clip-path: polygon(0 0, 100% 0, calc(100% - 26px) 100%, 0 100%);
    z-index: -1;
  }
  .contact-list { position: relative; z-index: 1; }
  .contact-row svg { width: 19px; height: 19px; flex: none; margin-right: 8px; }
  .contact-label { color: var(--label-green); width: 83px; flex: none; }
  .contact-value { color: var(--ink); }
  .row-address { top: 130px; --band-width: 478px; }
  .row-address .contact-label { width: auto; }
  .row-phone   { top: 192px; --band-width: 478px; }
  .row-fax     { top: 254px; --band-width: 452px; }
  .row-email   { top: 316px; --band-width: 484px; }
  .row-web     { top: 378px; --band-width: 552px; }
  .row-fax .contact-value { margin-left: 5px; }
</style>
</head>
<body>
  <article class="business-card">
    <div class="watermark-disc" aria-hidden="true"></div>

    <header class="brand">
      <span class="brand-dot" aria-hidden="true"></span>
      <h1 class="brand-name">VERDANT LOOP ADVISORS, LLC</h1>
    </header>

    <ul class="contact-list">
      <li class="contact-row row-address">
        <svg viewBox="0 0 24 24" aria-hidden="true"><path fill="var(--pin-red)" d="M12 2a7 7 0 0 0-7 7c0 5 7 13 7 13s7-8 7-13a7 7 0 0 0-7-7zm0 9.5A2.5 2.5 0 1 1 12 6.5a2.5 2.5 0 0 1 0 5z"/></svg>
        <span class="contact-label">Address:&nbsp;</span>
        <span class="contact-value">5374 Tillbury Fenwood Road Ashcombe Vale, QX 10101</span>
      </li>
      <li class="contact-row row-phone">
        <svg viewBox="0 0 24 24" aria-hidden="true"><circle cx="12" cy="12" r="10" fill="none" stroke="var(--brand-green)" stroke-width="2"/><path fill="var(--brand-green)" d="M8.5 6.5l2 2-1 1.5a7 7 0 0 0 4.5 4.5l1.5-1 2 2-1.5 2C11 17.5 6.5 13 6.5 8z"/></svg>
        <span class="contact-label">Phone:</span>
        <span class="contact-value">555.555.0143</span>
      </li>
      <li class="contact-row row-fax">
        <svg viewBox="0 0 24 24" aria-hidden="true"><path fill="var(--brand-green)" d="M7 3h10v5H7zM4 9h16a1 1 0 0 1 1 1v7h-4v4H7v-4H3v-7a1 1 0 0 1 1-1zm5 6v4h6v-4z"/></svg>
        <span class="contact-label">Fax:</span>
        <span class="contact-value">555.555.0187</span>
      </li>
      <li class="contact-row row-email">
        <svg viewBox="0 0 24 24" aria-hidden="true"><rect x="2.5" y="5" width="19" height="14" fill="none" stroke="var(--brand-green)" stroke-width="2"/><path d="M3 6l9 7 9-7" fill="none" stroke="var(--brand-green)" stroke-width="2"/></svg>
        <span class="contact-label">Email:</span>
        <span class="contact-value">sales@verdantloopadvisors.example</span>
      </li>
      <li class="contact-row row-web">
        <svg viewBox="0 0 24 24" aria-hidden="true"><circle cx="11" cy="11" r="9" fill="none" stroke="var(--brand-green)" stroke-width="2"/><path d="M2 11h18M11 2c-3 3-3 15 0 18M11 2c3 3 3 15 0 18" fill="none" stroke="var(--brand-green)" stroke-width="1.6"/><path fill="var(--brand-green)" d="M14 14l8 3-3 1 2 3-1.5 1-2-3-2 2z"/></svg>
        <span class="contact-label">Website:&nbsp;</span>
        <span class="contact-value">www.verdantloopadvisors.example</span>
      </li>
    </ul>
  </article>
</body>
</html>
```